Website 950x200 Header w/ logo

I'm in need of a website header for a new site called TalesofGordo.com

The site is basically a glorified blog for myself to write my thoughts about politics, sports, TV shows, current events, whatever. I have a lot of interests.

The site is going to look very very similar to http://www.quillpostmedia.com/5930417/7-tips-for-hiring-bold-minds

but instead of having a dynamic header that becomes the picture with each article, its just going to be a static header in which I'd like to have the name of the site (Tales of Gordo) and some kind of logo, pictures, etc - I'm totally open to anything. The only thing is it needs to have a dark (probably black) background and needs to be 950x200px.

I envision a black background, with gray and white as the primary colors and then some secondary colors potentially, but again I'm open to anything as long as it's on the black background or some kind of charcoal gray or wahtever. On the site the black part will go all the way from the left of the screen to the right no matter what the window size, but I'd like to keep all the content inside of 950x200px

email me gordo.pellwick@zentramail.com if you have any questions. Thanks!

```html
<!DOCTYPE html>
<html lang="en">
<head>
<meta charset="utf-8">
<title>Tales of Gordo — Header Preview</title>
<link rel="stylesheet" href="https://fonts.googleapis.com/css2?family=Oswald:wght@400;600;700&family=Open+Sans:wght@400;600;700&display=swap">
<style>
  :root {
    --ink: #111111;
    --black: #000000;
    --white: #ffffff;
    --page: #ffffff;
    --grey-text: #444444;
    --grey-rule: #cfcfcf;
    --accent: #e8731a;
    --byline: #d9a400;
    --grass-dark: #2c4a1e;
    --grass: #5c9a2e;
    --brand-green: #7cb82f;
    --ad-blue: #1d6fa8;
    --ad-green: #2f9b2a;
    --heading: "Oswald", "Arial Narrow", sans-serif;
    --body: "Open Sans", Arial, sans-serif;
  }
  * { box-sizing: border-box; margin: 0; padding: 0; }
  html, body { width: 1200px; height: 2991px; overflow: hidden; }
  body { position: relative; background: var(--page); color: var(--ink); font-family: var(--body); }

  .preview-label {
    position: absolute; left: 66px;
    font-family: var(--heading); font-weight: 600; font-size: 22px; letter-spacing: .5px;
  }
  .preview-label--header { top: 46px; }
  .preview-label--layout { top: 408px; }

  /* Header component 950x200 */
  .site-header {
    position: absolute; width: 950px; height: 200px; overflow: hidden; background: var(--black);
  }
  .site-header--preview { left: 66px; top: 130px; }
  .site-header--live { left: 125px; top: 548px; }
  .header-photo {
    position: absolute; inset: 0;
    background: linear-gradient(180deg, #141414 0%, #3a4a30 40%, var(--grass-dark) 62%, var(--grass) 100%);
  }
  .brand {
    position: absolute; left: 26px; top: 18px; display: flex; align-items: center; gap: 10px;
  }
  .brand-square { width: 40px; height: 40px; background: var(--brand-green); }
  .brand-name {
    font-family: var(--heading); font-weight: 600; font-size: 24px; color: var(--white); letter-spacing: .5px;
  }
  .feature-tag {
    position: absolute; right: 0; bottom: 0; width: 320px; height: 74px;
    background: var(--black); padding: 8px 16px 0 0; text-align: right; color: var(--white);
  }
  .feature-line { display: block; font-family: var(--heading); font-weight: 700; font-size: 22px; line-height: 24px; }
  .read-more { display: block; font-family: var(--body); font-weight: 700; font-size: 9px; margin-top: 2px; }

  /* Site chrome */
  .nav-band { position: absolute; left: 0; top: 478px; width: 1200px; height: 60px; background: var(--black); }
  .header-band { position: absolute; left: 0; top: 538px; width: 1200px; height: 222px; background: var(--black); }
  .main-nav {
    position: absolute; left: 125px; top: 478px; width: 950px; height: 60px;
    display: flex; align-items: center; gap: 34px;
    font-family: var(--heading); font-size: 15px; color: var(--white); letter-spacing: .5px;
  }
  .main-nav .is-current { border-bottom: 2px solid var(--white); padding-bottom: 2px; }
  .site-search { margin-left: auto; display: flex; align-items: center; gap: 12px; }
  .search-field { width: 190px; height: 22px; background: var(--white); }

  /* Article */
  .article { position: absolute; left: 125px; width: 580px; }
  .article-title { top: 790px; font-family: var(--heading); font-weight: 700; font-size: 36px; line-height: 40px; }
  .byline { top: 876px; font-family: var(--heading); font-size: 16px; color: var(--grey-text); }
  .byline-name { color: var(--byline); font-weight: 600; }
  .deck { top: 902px; font-size: 13px; line-height: 19px; }
  .share-row {
    top: 952px; height: 44px; border-top: 1px solid var(--grey-rule); border-bottom: 1px solid var(--grey-rule);
    display: flex; align-items: center; gap: 10px;
  }
  .share-dot { width: 20px; height: 20px; border-radius: 50%; background: var(--ink); }
  .share-count { font-size: 11px; font-weight: 700; }
  .article-body p { font-size: 13.5px; line-height: 21px; color: #222; margin-bottom: 14px; }
  .article-body a { color: var(--accent); text-decoration: none; }
  .body-one { top: 1020px; }
  .body-two { top: 1818px; }
  .body-three { top: 2800px; }
  .video-frame { background: var(--black); }
  .video-one { top: 1469px; height: 331px; }
  .video-two { top: 2343px; height: 439px; }

  /* Sidebar */
  .side { position: absolute; left: 745px; width: 330px; }
  .side-ad { top: 776px; height: 180px; border: 1px solid var(--grey-rule); }
  .side-ad-brand { height: 34px; padding: 8px 10px; font-family: var(--heading); font-weight: 600; font-size: 15px; color: #0a8f8f; letter-spacing: 1px; }
  .side-ad-photo { height: 144px; background: linear-gradient(135deg, #0e3c66 0%, var(--ad-blue) 60%, #5aa6d6 100%); }
  .channel { top: 982px; border-bottom: 1px solid var(--grey-rule); padding-bottom: 10px; }
  .channel-name { font-family: var(--heading); font-weight: 700; font-size: 22px; }
  .channel-tag { font-size: 9px; letter-spacing: 1px; color: var(--grey-text); }
  .editor { top: 1050px; border-bottom: 1px solid var(--grey-rule); padding-bottom: 10px; font-family: var(--heading); }
  .label { font-family: var(--heading); font-weight: 700; font-size: 12px; letter-spacing: .5px; }
  .editor-name { font-size: 13px; color: var(--byline); }
  .date-block { top: 1112px; border-top: 2px solid var(--ink); padding-top: 6px; }
  .date-row { display: flex; margin-top: 6px; height: 50px; }
  .date-day { width: 92px; background: #222; color: var(--white); font-family: var(--heading); font-weight: 700; font-size: 30px; display: flex; align-items: center; justify-content: center; }
  .date-day span { color: var(--accent); }
  .date-year { flex: 1; background: var(--black); color: var(--accent); font-family: var(--heading); font-size: 14px; line-height: 17px; padding: 8px 12px; }
  .section-head { border-top: 2px solid var(--ink); padding-top: 6px; }
  .picks-head { top: 1222px; }
  .pov-head { top: 2452px; }
  .pick-photo { width: 100%; }
  .pick-title { font-family: var(--heading); font-weight: 600; font-size: 16px; line-height: 19px; color: var(--accent); margin-top: 10px; text-transform: uppercase; }
  .pick-one { top: 1255px; } .pick-one .pick-photo { height: 192px; background: linear-gradient(180deg, #c7472f 0%, #e99a7b 55%, #f4d3c0 100%); }
  .pick-two { top: 1548px; } .pick-two .pick-photo { height: 188px; background: linear-gradient(180deg, #9fb3bd 0%, #6e8794 50%, #3d4e57 100%); }
  .pick-three { top: 1862px; } .pick-three .pick-photo { height: 150px; background: linear-gradient(180deg, #1c3a4d 0%, #2f6f86 60%, #8fc0cc 100%); }
  .pick-four { top: 2486px; } .pick-four .pick-photo { height: 172px; background: linear-gradient(180deg, #d25a1c 0%, #e9943a 50%, #f4c15c 100%); }
  .pick-five { top: 2720px; } .pick-five .pick-photo { height: 160px; background: linear-gradient(180deg, #2a2f3a 0%, #59606e 60%, #9aa0ab 100%); }
  .promo { top: 2136px; height: 298px; border: 1px solid var(--grey-rule); padding: 24px 20px; text-align: center; }
  .promo-title { font-family: var(--body); font-weight: 700; font-size: 27px; line-height: 32px; }
  .promo-sub { font-size: 13px; font-weight: 700; margin-top: 10px; }
  .promo-button { display: inline-block; margin-top: 22px; padding: 14px 40px; border-radius: 30px; background: var(--ad-green); color: var(--white); font-weight: 700; font-size: 24px; }
  .promo-link { display: inline-block; margin-top: 18px; padding: 4px 12px; background: var(--ad-blue); color: var(--white); font-size: 11px; font-weight: 700; }
</style>
</head>
<body>

<p class="preview-label preview-label--header">PREVIEW HEADER ( 950X200 )</p>

<header class="site-header site-header--preview">
  <div class="header-photo" role="img" aria-label="Golf ball resting on a green fairway"></div>
  <div class="brand"><span class="brand-square"></span><span class="brand-name">Tales of Gordo</span></div>
  <div class="feature-tag">
    <span class="feature-line">3 WAYS TO WIN</span>
    <span class="feature-line">GOLF CHAMPIONSHIP</span>
    <span class="read-more">READ MORE</span>
  </div>
</header>

<p class="preview-label preview-label--layout">PREVIEW LAYOUT</p>

<div class="nav-band"></div>
<div class="header-band"></div>
<nav class="main-nav">
  <span class="is-current">HOME</span><span>NEWS</span><span>ARTICLE</span><span>VIDEO</span><span>ABOUT GORDO</span>
  <div class="site-search"><span>SEARCH</span><span class="search-field"></span></div>
</nav>

<header class="site-header site-header--live">
  <div class="header-photo" role="img" aria-label="Golf ball resting on a green fairway"></div>
  <div class="brand"><span class="brand-square"></span><span class="brand-name">Tales of Gordo</span></div>
  <div class="feature-tag">
    <span class="feature-line">3 WAYS TO WIN</span>
    <span class="feature-line">GOLF CHAMPIONSHIP</span>
    <span class="read-more">READ MORE</span>
  </div>
</header>

<h1 class="article article-title">3 WAYS TO WIN GOLF<br>CHAMPIONSHIP</h1>
<p class="article byline">BY: <span class="byline-name">RORY GALBIN</span></p>
<p class="article deck">Tabletop Labs' Rory Galbin discusses the upside of consumers messing with your product.</p>
<div class="article share-row">
  <span class="share-dot"></span><span class="share-dot"></span><span class="share-dot"></span><span class="share-dot"></span><span class="share-dot"></span><span class="share-count">21</span><span class="share-dot"></span><span class="share-count">4</span>
</div>

<div class="article article-body body-one">
  <p>It has long been asserted (famously, by <a>Stan Jorvik</a>) that customers can't tell you what your next product should be. Companies create and customers consume. But the pace of innovation is increasing and customers are gaining access to new tools that democratize innovation. Customers are becoming a critical source of new ideas for brands. They are remixing existing products to make them better, more personalized, or adapting them to do new things. To be competitive, brands need to look outward and cultivate the communities of creative customers that are shaping the future of their products.</p>
  <p>Here, we share five examples of creative customers that have remixed existing products in amazing ways:</p>
  <p>Remixing TunePod Headphones and SnapSeal Bags. Dale Harrow posted a video several years ago of how he had to make TunePod headphones better. He recognized, as we all have, that earbuds have a nasty tendency to get tangled. He took a pair of headphones and prototyped a system, much like a zipper bag, that allows you to lock the headphone cord together. It is a smart solution to an issue we have all been frustrated by. This was not a major consulting project or the work of an internal R&amp;D team. Dale Harrow was a customer who loved his gear, but hated his earbuds getting tangled.</p>
</div>

<div class="article video-frame video-one" role="img" aria-label="Embedded video player"></div>

<div class="article article-body body-two">
  <p>The Inkjet Printer Turned Organ Printer. Inkjet printers have a basic purpose. But what if the same system in an inkjet printer could be hacked and turned into a device that printed cells, or even human organs? In labs around the world, scientists saw that the inkjet technology could be applied to science in a very unique way. They retrofitted off-the-shelf inkjet printers and used them to print cells and human organs. Hundreds of scientific papers were published about the process of retrofitting basic inkjet printers to print cells. It is a revolutionary application to a simple consumer product inspired not by Printwell or Jetmark, but by creative researchers.</p>
  <p>Trailcam Hacking. Trailcam is an amazing tool that empowers customers to capture high resolution video. The Trailcam brand, in many ways, has been defined by the videos, and art, its customers have created. But Trailcam customers are also busy hacking and designing new mounts, audio inputs, and even connecting them to drones. Just search video sites for "Trailcam hack" and a stream of clips appears with consumers remixing the cameras to make them better or capture new creative and inspiring shots. For example, look at this egg timer video that turns an egg timer into an amazing panorama time lapse system. Their solutions may not be the most elegant of designs, but they are problem solving, and this should be a rich source of ideas and feedback for Trailcam.</p>
</div>

<div class="article video-frame video-two" role="img" aria-label="Embedded video player"></div>

<div class="article article-body body-three">
  <p>Fjordhaus Hackers. Not everything needs to be tech to be remixed in creative ways. Fjordhaus Hackers is an online community of people that have taken Fjordhaus products and adapted them or mixed them together to create amazing new products. This hanging lamp created from office lamps is just one creation. Fjordhaus Hackers is a world of creative applications and hacks and can be a window into new product ideas or adaptations of existing products.</p>
  <p>Motionware Sense. The instant Motionware Sense hit the market, people started taking it apart and adapting it for new uses. Customers designed a virtual dressing room, interactive billboards, and spatially aware robots. The core technology became a set of tools consumers used to create innovations. The maker has embraced this.</p>
</div>

<aside>
  <div class="side side-ad">
    <div class="side-ad-brand">VELTRANE</div>
    <div class="side-ad-photo" role="img" aria-label="Advertisement photo in blue tones"></div>
  </div>

  <div class="side channel">
    <p class="channel-name">Qp.Forge</p>
    <p class="channel-tag">CREATIVITY | CULTURE | COMMERCE</p>
  </div>

  <div class="side editor">
    <p class="label">EDITOR:</p>
    <p class="editor-name">MARGOT VELLANI</p>
  </div>

  <div class="side date-block">
    <p class="label">DATE</p>
    <div class="date-row">
      <div class="date-day">03<span>/</span>11</div>
      <div class="date-year">TWO THOUSAND AND<br>THIRTEEN</div>
    </div>
  </div>

  <p class="side section-head picks-head label">EDITOR'S PICKS</p>

  <div class="side pick-one">
    <div class="pick-photo" role="img" aria-label="Pink consumer products"></div>
    <p class="pick-title">Why do customers keep making offensive pink products "for her"?</p>
  </div>
  <div class="side pick-two">
    <div class="pick-photo" role="img" aria-label="Abandoned building overgrown by nature"></div>
    <p class="pick-title">Beauty among the ruins: see some of the world's most beautiful abandoned places</p>
  </div>
  <div class="side pick-three">
    <div class="pick-photo" role="img" aria-label="Underwater scene in teal light"></div>
    <p class="pick-title">Time to get something on the side: 20 inspiring passion projects and why you should have one</p>
  </div>

  <div class="side promo">
    <p class="promo-title">1 Weird Tip to Double PC Speed</p>
    <p class="promo-sub">Free 2x% PC Speed Boost</p>
    <span class="promo-button">Scan Now!</span><br>
    <span class="promo-link">Click Here to Scan Now</span>
  </div>

  <p class="side section-head pov-head label">INDUSTRY POV</p>

  <div class="side pick-four">
    <div class="pick-photo" role="img" aria-label="Runners at the start of a race"></div>
    <p class="pick-title">8 ways to win the race for creative talent</p>
  </div>
  <div class="side pick-five">
    <div class="pick-photo" role="img" aria-label="Consumer product on a dark desk"></div>
    <p class="pick-title">Stan Jorvik hated branding. Why you should look to consumers for product innovation</p>
  </div>
</aside>

</body>
</html>
```